Saucy Velvet Impz Business Card

We need business cards designed for our consultants to use and hand out to customers.
We are an Adult party plan company (like Crelvaware but sex toys and lingerie)
We would like bright colours pinks, purples.
The cards need our logo
Space for the reps phone number email address and name.
We need our website on it www.saucyvelvetimps.com.au

```html
<!DOCTYPE html>
<html lang="en">
<head>
<meta charset="utf-8">
<title>Saucy Velvet Impz Business Card</title>
<link rel="stylesheet" href="https://fonts.googleapis.com/css2?family=Crimson+Text:wght@700&family=Didact+Gothic&display=swap">
<style>
  :root {
    --page: #efeae6;
    --pink-deep: #ec2b8c;
    --pink-mid: #f265a8;
    --pink-soft: #f7a8cd;
    --pink-mist: #fbd3e5;
    --paper: #f4f3f4;
    --paper-shade: #e2e0e2;
    --ink: #1e1e1e;
    --label: #3a3a3a;
  }
  * { box-sizing: border-box; margin: 0; padding: 0; }
  html, body { width: 1200px; height: 1000px; overflow: hidden; }
  body {
    background: var(--page);
    display: flex;
    flex-direction: column;
    align-items: center;
    justify-content: center;
    gap: 60px;
  }
  .card {
    width: 700px;
    height: 400px;
    border-radius: 34px;
    position: relative;
    overflow: hidden;
    box-shadow: 0 10px 30px rgba(0,0,0,0.15);
  }

  /* Front */
  .card-front {
    background:
      radial-gradient(ellipse at 20% 80%, rgba(255,255,255,0.35), transparent 55%),
      radial-gradient(ellipse at 70% 20%, rgba(255,255,255,0.18), transparent 50%),
      linear-gradient(135deg, var(--pink-soft) 0%, var(--pink-mid) 40%, var(--pink-deep) 100%);
    display: flex;
    align-items: center;
    justify-content: center;
  }
  .brand-lockup {
    display: flex;
    align-items: center;
    gap: 16px;
  }
  .brand-dot {
    width: 44px;
    height: 44px;
    border-radius: 50%;
    background: var(--pink-mist);
  }
  .brand-name {
    font-family: "Crimson Text", Georgia, serif;
    font-weight: 700;
    font-size: 46px;
    color: var(--pink-mist);
    letter-spacing: 0.5px;
  }

  /* Back */
  .card-back {
    background:
      radial-gradient(ellipse at 60% 40%, #ffffff, transparent 60%),
      linear-gradient(160deg, var(--paper) 0%, var(--paper-shade) 100%);
  }
  .back-decoration {
    position: absolute;
    left: 0;
    top: 0;
    width: 300px;
    height: 400px;
    background: radial-gradient(ellipse at 45% 45%, rgba(242,101,168,0.35), rgba(242,101,168,0) 70%);
  }
  .back-content {
    position: absolute;
    right: 48px;
    top: 50px;
    bottom: 40px;
    display: flex;
    flex-direction: column;
    align-items: flex-end;
    text-align: right;
  }
  .back-brand {
    font-family: "Crimson Text", Georgia, serif;
    font-weight: 700;
    font-size: 50px;
    color: var(--pink-mid);
    line-height: 1;
  }
  .rep-name {
    font-family: "Didact Gothic", Arial, sans-serif;
    font-size: 32px;
    color: var(--ink);
    margin-top: 18px;
  }
  .contact-list {
    margin-top: auto;
    list-style: none;
    font-family: "Didact Gothic", Arial, sans-serif;
    display: flex;
    flex-direction: column;
    gap: 8px;
  }
  .contact-label {
    display: block;
    font-size: 15px;
    color: var(--label);
  }
  .contact-value {
    display: block;
    font-size: 19px;
    color: var(--pink-deep);
    letter-spacing: 0.5px;
  }
</style>
</head>
<body>
  <section class="card card-front" aria-label="Business card front">
    <div class="brand-lockup">
      <span class="brand-dot"></span>
      <span class="brand-name">Saucy Velvet Impz</span>
    </div>
  </section>

  <section class="card card-back" aria-label="Business card back">
    <div class="back-decoration" role="img" aria-label="Large faint pink brand decoration"></div>
    <div class="back-content">
      <h1 class="back-brand">Saucy Velvet Impz</h1>
      <p class="rep-name">Your Name</p>
      <ul class="contact-list">
        <li><span class="contact-label">phone:</span><span class="contact-value">0400 555 218</span></li>
        <li><span class="contact-label">email:</span><span class="contact-value">info@saucyvelvetimps.com.au</span></li>
        <li><span class="contact-label">web:</span><span class="contact-value">www.saucyvelvetimps.com.au</span></li>
      </ul>
    </div>
  </section>
</body>
</html>
```